Website design for dressage horse training business

Looking to develop a new website design for a dressage horse training website. We want to change from a single landing page to one with multiple pages.
You are free to use your creativity to design the main landing page. This is the only page you need to design at this point. I would encourage looking at other Dressage Training websites to get a feel for what is typically on them. A few websites are listed below although I think the design of them could be better.
Notes:
- Menu to include: Home, Services, News Room, Blog, About Us, Contact,
- FAQ section on main page
- Logo to remain the same - the logo attached is not the correct color so change to match existing color.
- Change 'Sponsors' to 'Partnerships' on main page
Here is the link to the current site:
https://lindenridgestables.com/
Example sites
https://www.crestwoodsporthorsesco.com/
https://corinnalavelledressage.com/
Target Market(s)
Older women with disposable income
Number of Pages Required
1 page
Look and feel
Each slider illustrates characteristics of the customer's brand and the style your logo design should communicate.

```html
<!DOCTYPE html>
<html lang="en">
<head>
<meta charset="utf-8">
<title>Linden Ridge Stables – Dressage &amp; Sport Horse Training</title>
<link href="https://fonts.googleapis.com/css2?family=Libre+Baskerville:wght@400;700&family=Open+Sans:wght@400;600;700&display=swap" rel="stylesheet">
<style>
:root{
  --tan:#b8956b;
  --tan-btn:#c3a17a;
  --tan-light:#d9c3a6;
  --ink:#2b2b2b;
  --muted:#6b6b6b;
  --panel:#f2f2f2;
  --white:#ffffff;
  --line:#aaaaaa;
}
*{box-sizing:border-box;margin:0;padding:0}
html,body{width:1200px;height:4675px;overflow:hidden}
body{position:relative;background:var(--white);font-family:"Open Sans",sans-serif;color:var(--ink)}
.abs{position:absolute}

/* nav */
.site-nav{position:absolute;top:0;left:0;width:1200px;height:100px;background:var(--white);border-bottom:3px solid var(--tan-light);z-index:2}
.nav-link{position:absolute;top:42px;font-size:14px;color:var(--ink)}
.nav-link.active{border-bottom:2px solid var(--tan);padding-bottom:8px}
.brand{position:absolute;left:0;width:1200px;top:24px;text-align:center;font-family:"Libre Baskerville",serif;font-size:30px;color:var(--tan);letter-spacing:1px}

/* hero */
.hero{position:absolute;top:100px;left:0;width:1200px;height:440px;border-bottom:3px solid var(--tan)}
.hero-photo{position:absolute;inset:0;background:linear-gradient(100deg,#d8c7ad 0%,#c9b292 45%,#a9825f 75%,#c4ac8c 100%)}
.hero h1{position:absolute;left:120px;top:112px;font-family:"Libre Baskerville",serif;font-weight:400;font-size:36px;line-height:47px;color:#2a2a2a}
.hero-loc{position:absolute;left:128px;top:228px;font-size:22px;color:#2a2a2a;display:flex;align-items:center;gap:16px}
.btn{position:absolute;display:flex;align-items:center;justify-content:center;font-size:13px;font-weight:600;border-radius:24px}
.btn-light{left:127px;top:286px;width:138px;height:46px;background:var(--white);color:var(--ink);border:2px solid var(--tan-light)}
.btn-tan{left:295px;top:286px;width:136px;height:46px;background:var(--tan-btn);color:var(--white)}

.emblem{position:absolute;left:524px;top:474px;width:152px;height:152px;border-radius:50%;background:var(--white);border:3px solid var(--tan-light);display:flex;align-items:center;justify-content:center;text-align:center;font-family:"Libre Baskerville",serif;font-size:16px;color:var(--tan);z-index:3}

.section-title{position:absolute;left:0;width:1200px;text-align:center;font-family:"Libre Baskerville",serif;font-size:36px;color:var(--ink)}
.section-title .amp{color:var(--tan)}
.section-sub{position:absolute;left:0;width:1200px;text-align:center;font-size:13px;line-height:23px;color:var(--muted)}

.card{position:absolute;top:760px;width:404px;height:349px;background:var(--panel);border:1px solid #d8d8d8;box-shadow:0 3px 8px rgba(0,0,0,.15)}
.card h3{position:absolute;top:48px;left:0;width:100%;text-align:center;font-size:21px;font-weight:400}
.card p{position:absolute;left:47px;top:114px;width:310px;font-size:14px;line-height:20px}
.card .card-btn{position:absolute;left:123px;top:262px;width:160px;height:42px;background:var(--tan-btn);color:var(--white);font-size:14px;font-weight:600;display:flex;align-items:center;justify-content:center;box-shadow:0 3px 6px rgba(0,0,0,.2)}
.divider-v{position:absolute;left:599px;top:804px;width:3px;height:263px;background:var(--tan)}

/* about */
.about{position:absolute;top:1187px;left:0;width:1200px;height:775px;background:var(--panel)}
.about-photo{position:absolute;left:0;top:0;width:600px;height:775px;background:linear-gradient(160deg,#6f7d4c 0%,#98a06c 35%,#b9a78a 65%,#8c6b4f 100%)}
.about h2{position:absolute;left:699px;top:65px;font-family:"Libre Baskerville",serif;font-weight:400;font-size:34px;padding-bottom:14px;border-bottom:3px solid var(--tan)}
.social{position:absolute;top:77px;display:flex;gap:12px;left:980px}
.social span{width:24px;height:24px;border:2.5px solid var(--tan);border-radius:5px}
.about-text{position:absolute;left:695px;top:155px;width:410px;font-size:14.5px;line-height:22.3px;font-weight:600;color:#222}
.about-text p+p{margin-top:12px}

/* partnerships */
.partner h4{position:absolute;top:2115px;font-family:"Libre Baskerville",serif;font-weight:400;font-size:21px;color:var(--tan)}
.partner p{position:absolute;top:2166px;width:395px;font-size:13px;line-height:22.3px;color:#3a3a3a}
.read-more{position:absolute;top:2380px;font-size:13px;color:var(--tan);border-bottom:2px solid var(--tan-light);padding-bottom:4px}
.partner-name{position:absolute;top:2378px;font-size:14px;font-weight:600;color:var(--ink);white-space:nowrap}

/* for sale */
.sale{position:absolute;top:2505px;left:0;width:1200px;height:989px;background:var(--panel)}
.sale-title{position:absolute;top:63px;left:0;width:1200px;text-align:center;font-family:"Libre Baskerville",serif;font-size:36px;color:var(--tan)}
.sale-sub{position:absolute;top:130px;left:0;width:1200px;display:flex;justify-content:center;align-items:center;gap:30px;font-size:14px;color:var(--tan)}
.sale-sub i{width:64px;height:2px;background:var(--tan)}
.sale-text{position:absolute;left:122px;top:202px;width:580px;font-size:14.5px;line-height:22.3px;color:#222}
.sale-text p+p{margin-top:24px}
.sale-photo{position:absolute;left:800px;top:198px;width:280px;height:368px;border:3px solid var(--tan-light);background:linear-gradient(180deg,#cfd6c4 0%,#7c6a59 45%,#3b2a22 100%);box-shadow:0 3px 8px rgba(0,0,0,.2)}
.faq-bracket{position:absolute;left:368px;top:668px}
.faq-title{position:absolute;top:615px;left:0;width:1200px;text-align:center;font-family:"Libre Baskerville",serif;font-size:36px;line-height:50px;z-index:1}
.faq-title span{background:var(--panel);padding:0 18px}
.faq-q{position:absolute;left:214px;width:325px;height:64px;background:var(--white);border:1px solid var(--tan-light);box-shadow:0 2px 6px rgba(0,0,0,.12);display:flex;align-items:center;padding-left:38px;font-size:14px;color:var(--tan)}
.faq-a{position:absolute;left:543px;top:697px;width:439px;height:202px;background:var(--white);border:1px solid var(--tan-light);box-shadow:0 2px 6px rgba(0,0,0,.12);padding:24px 40px 0 42px;font-size:13px;line-height:19.5px}

/* news */
.news-card{position:absolute;top:3733px;width:285px;height:293px;border:2px solid var(--tan-light);background:var(--white);box-shadow:0 3px 6px rgba(0,0,0,.12)}
.news-card p{position:absolute;left:30px;top:30px;width:225px;font-size:13.5px;line-height:19.5px}
.news-card .rule{position:absolute;left:14px;right:14px;top:208px;height:2px;background:#d8d8d8}
.news-day{position:absolute;left:38px;top:250px;font-size:16px;font-weight:600;color:var(--tan)}
.news-date{position:absolute;right:38px;top:250px;font-size:16px;font-weight:600}
.see-more{position:absolute;left:525px;top:4082px;width:150px;height:42px;background:var(--tan-btn);color:var(--white);font-size:13px;font-weight:600;display:flex;align-items:center;justify-content:center;box-shadow:0 3px 6px rgba(0,0,0,.2)}

/* footer */
.footer{position:absolute;top:4202px;left:0;width:1200px;height:408px;background:var(--panel)}
.footer h2{position:absolute;left:123px;top:88px;font-family:"Libre Baskerville",serif;font-weight:400;font-size:24px;padding-bottom:10px;border-bottom:3px solid var(--tan)}
.footer .blurb{position:absolute;left:123px;top:160px;width:300px;font-size:13px;line-height:22px}
.footer .fsocial{position:absolute;left:123px;top:308px;display:flex;gap:14px;align-items:center}
.footer .fsocial .icon{width:24px;height:24px;border:2.5px solid var(--tan);border-radius:5px}
.footer .phone{margin-left:24px;font-size:14px}
.footer nav a{position:absolute;left:523px;font-size:14px;color:var(--ink);text-decoration:none}
.map{position:absolute;left:717px;top:0;width:483px;height:408px;background:linear-gradient(135deg,#e6e9de 0%,#dfe3d5 50%,#cfdbe6 100%)}
.copyright{position:absolute;top:4620px;left:0;width:1200px;text-align:center;font-size:11px;color:#444}
</style>
</head>
<body>

<header class="site-nav">
  <a class="nav-link active" style="left:120px">Home</a>
  <a class="nav-link" style="left:203px">Services</a>
  <a class="nav-link" style="left:299px">About Us</a>
  <div class="brand">Linden Ridge</div>
  <a class="nav-link" style="left:810px">News Room</a>
  <a class="nav-link" style="left:929px">Blog</a>
  <a class="nav-link" style="left:1005px">Contact</a>
</header>

<section class="hero">
  <div class="hero-photo" role="img" aria-label="Close view of a chestnut horse's legs stepping across a sand arena with the rider's boots above"></div>
  <h1>Central Iowa's Premier Dressage<br>&amp; Sport Horse Training</h1>
  <div class="hero-loc">Located outside Des Moines, Iowa
    <svg width="18" height="24" viewBox="0 0 18 24"><path d="M9 1C4.6 1 1.5 4.3 1.5 8.4 1.5 14 9 22.5 9 22.5S16.5 14 16.5 8.4C16.5 4.3 13.4 1 9 1z" fill="none" stroke="#b8956b" stroke-width="2"/><circle cx="9" cy="8.5" r="2.8" fill="none" stroke="#b8956b" stroke-width="2"/></svg>
  </div>
  <a class="btn btn-light">Our Services</a>
  <a class="btn btn-tan">Contact Us</a>
</section>
<div class="emblem">Linden<br>Ridge</div>

<h2 class="section-title" style="top:632px">Training <span class="amp">&amp;</span> Lessons</h2>
<p class="section-sub" style="top:686px">Lorem ipsum dolor sit amet, consetetur sadipscing elitr, sed<br>diam nonumy eirmod tempor invidunt ut labore et dolore magna</p>

<article class="card" style="left:122px">
  <h3>Training</h3>
  <p>Linden Ridge offers both full and half time training options with Clara Whitfield. There is much flexibility with both rides and/or lessons weekly in the training packages...</p>
  <a class="card-btn">Know More</a>
</article>
<div class="divider-v"></div>
<article class="card" style="left:675px">
  <h3>Lessons</h3>
  <p>Lessons are available for all ages of riders. Clara thoroughly enjoys working with accomplished riders looking to succeed in the show ring, as well as riders...</p>
  <a class="card-btn">Read More</a>
</article>

<section class="about">
  <div class="about-photo" role="img" aria-label="Rider in a dark show coat and helmet on a brown and white pinto horse in an outdoor arena"></div>
  <h2>About Us</h2>
  <div class="social"><span></span><span></span><span></span></div>
  <div class="about-text">
    <p>FEI rider and trainer, Clara Whitfield began her riding career at a young age. She went up through the ranks of Junior Riding Club and with an emphasis and focus in eventing. During college, Clara worked for a small breeder starting young horses. Clara loves starting young horses including starting and guiding them in a correct and quiet way to help them flourish. Her training focuses on gymnastic training incorporating ground work/lunging/long lining, jumping, cavelletti and regular hacking and trail riding.</p>
    <p>Clara is a national federation Silver Medalist having competed through the FEI levels of I1. A learner at heart, Clara regularly clinics and rides with other trainers and accomplished dressage riders from across the nation to continue to pursue her goal of competing at the Grand Prix.</p>
    <p>Clara has attended the L Program as well as the Instructor/Trainer program to continue her growth as a trainer and rider. Clara trains and competes yearly in the winter season in Wellington, Florida to further her knowledge and development to share with her students!</p>
  </div>
</section>

<h2 class="section-title" style="top:2022px">Partnerships</h2>
<div class="partner">
  <h4 style="left:121px">Heritage Saddlery</h4>
  <p style="left:120px">Heritage Saddlery is constantly designing and researching saddles and riders to find the right blend of design and craftsmanship to fit today's demands. Every saddle's detail is carefully checked to be sure the workmanship and quality is there. All saddles are anatomically designed for horse and rider, hand-crafted from the finest leathers, and manufactured using the most technically advanced methods and features available.</p>
  <a class="read-more" style="left:121px">Read More</a>
  <span class="partner-name" style="left:376px">Heritage Saddlery</span>

  <h4 style="left:685px">Marlow's Saddlery</h4>
  <p style="left:684px">My goal is to provide the best possible fit for both horse and rider whether it is a saddle you already own, one you have on trial, or one that I carry. Being a Qualified Saddle Fitter by the Guild of Master Saddle Fitters allows me to work with all saddle types and brands. In addition, I carry a broad range of saddles to fit your needs, both new and used. Having a multitude of saddles in my stock makes saddle shopping much easier for you.</p>
  <a class="read-more" style="left:685px">Read More</a>
  <span class="partner-name" style="left:965px">Marlow's Saddlery</span>
</div>

<section class="sale">
  <h2 class="sale-title">For Sale</h2>
  <div class="sale-sub"><i></i>Mariner's Promise<i></i></div>
  <div class="sale-text">
    <p>Mariner's Promise, "Finn," (Mariner x Silver Pilot) is a 2012, 16hh imported Hanoverian. Finn is an incredibly quiet and kind horse. He is ridden by both an amatuer and child rider. He loves to hack and is very quiet alone and with a group of horses. He has shown through first level with scores into the 70's at both training and first level.</p>
    <p>Finn is currently solidly schooling all of second level, as well as half passes and flying changes from third level. Finn has 3 very easy to ride gaits and it is easy for riders to sit his trot. Very quiet and well mannered on the ground with vet, farrier and clipping. He has lovely confirmation with a striking head. He is regularly admired at shows! Finn is very versatile and game and also loves to jump!</p>
  </div>
  <div class="sale-photo" role="img" aria-label="Dark bay horse in a bridle standing in front of flowering white shrubs"></div>

  <svg class="faq-bracket" width="464" height="32"><path d="M2 30V2H462V30" fill="none" stroke="#aaa" stroke-width="2"/></svg>
  <h2 class="faq-title"><span>FAQs</span></h2>
  <div class="faq-q" style="top:697px">How long is the training course ?</div>
  <svg class="abs" style="left:523px;top:716px;z-index:2" width="28" height="28"><circle cx="14" cy="14" r="12" fill="#fff" stroke="#b8956b" stroke-width="1.5"/><path d="M11 8l6 6-6 6" fill="none" stroke="#b8956b" stroke-width="1.5"/></svg>
  <div class="faq-q" style="top:766px">How much is the training fee ?</div>
  <div class="faq-q" style="top:835px">How many trainees are there ?</div>
  <div class="faq-a">Lorem ipsum dolor sit amet, consetetur sadipscing elitr, sed diam nonumy eirmod tempor invidunt ut labore et dolore magna aliquyam erat, sed diam voluptua. At vero eos et accusam et justo duo dolores et ea rebum. Stet clita kasd gubergren, no sea takimata sanctus est Lorem ipsum dolor sit amet. Lorem ipsum dolor sit amet, consetetur sadipscing elitr, sed diam nonumy eirmod tempor invidunt ut</div>
</section>

<h2 class="section-title" style="top:3555px">Latest News</h2>
<p class="section-sub" style="top:3630px">Lorem ipsum dolor sit amet, consetetur sadipscing elitr, sed<br>diam nonumy eirmod tempor invidunt ut labore et dolore magna</p>

<article class="news-card" style="left:122px"><p>Lorem ipsum dolor sit amet, consetetur sadipscing elitr, sed diam nonumy eirmod tempor invidunt ut labore et dolore magna aliquyam erat, sed diam voluptua. At vero</p><div class="rule"></div><span class="news-day">SAT</span><span class="news-date">February 10</span></article>
<article class="news-card" style="left:459px"><p>Lorem ipsum dolor sit amet, consetetur sadipscing elitr, sed diam nonumy eirmod tempor invidunt ut labore et dolore magna aliquyam erat, sed diam voluptua. At vero</p><div class="rule"></div><span class="news-day">SUN</span><span class="news-date">February 11</span></article>
<article class="news-card" style="left:796px"><p>Lorem ipsum dolor sit amet, consetetur sadipscing elitr, sed diam nonumy eirmod tempor invidunt ut labore et dolore magna aliquyam erat, sed diam voluptua. At vero</p><div class="rule"></div><span class="news-day">FRI</span><span class="news-date">February 23</span></article>
<a class="see-more">See more</a>

<footer class="footer">
  <h2>Contact Me</h2>
  <p class="blurb">If you are interested in learning more about Linden Ridge's services or availability for training or lessons, please contact us below!</p>
  <div class="fsocial"><span class="icon"></span><span class="icon"></span><span class="icon"></span><span class="phone">+ 515-555-0187</span></div>
  <nav>
    <a style="top:88px">Home</a>
    <a style="top:129px">Services</a>
    <a style="top:170px">About Us</a>
    <a style="top:211px">News Room</a>
    <a style="top:252px">Blog</a>
    <a style="top:293px">Contact Us</a>
  </nav>
  <div class="map" role="img" aria-label="Road map of the area east of Des Moines showing nearby towns and the farm's location"></div>
</footer>
<p class="copyright">© 2020 Linden Ridge Stables All Rights Reserved.</p>

</body>
</html>
```